Brochure design for Velicor

Create a bi-fold A5 size brochure. I have attached our logo and the written content to be included in the brochure. So the brochure will have a total of 4 pages (front page, inner two pages, back page). End source files need to include final printable brochure as well as editable files.

```html
<!DOCTYPE html>
<html lang="en">
<head>
<meta charset="utf-8">
<title>Velicor Brochure – Outer Spread</title>
<link href="https://fonts.googleapis.com/css2?family=Cinzel:wght@400;700&family=Open+Sans:wght@400;600;700&display=swap" rel="stylesheet">
<style>
  :root {
    --canvas-bg: #d9dadc;
    --brand-blue: #2f63ad;
    --deep-blue: #16348a;
    --mid-blue: #3f78c4;
    --brand-green: #8cc63f;
    --dark-green: #5a8f2a;
    --paper: #ffffff;
    --paper-grey: #eceef1;
    --ink: #2b3a55;
    --photo-lab: #cfdbe8;
    --photo-people: #8fa6b8;
    --photo-dna: #3c6fa8;
  }
  * { margin: 0; padding: 0; box-sizing: border-box; }
  html, body { width: 1200px; height: 789px; overflow: hidden; }
  body {
    background: var(--canvas-bg);
    font-family: "Open Sans", Arial, sans-serif;
    display: flex; align-items: center; justify-content: center;
  }
  .spread {
    width: 1080px; height: 764px; display: flex;
    box-shadow: 0 8px 24px rgba(0,0,0,.25);
  }
  .page { position: relative; width: 540px; height: 764px; overflow: hidden; background: var(--paper); }

  /* Back page */
  .back-visual {
    position: absolute; inset: 0 0 auto 0; height: 520px;
    background: radial-gradient(ellipse at 30% 30%, #3e74c9 0%, #1c3f9c 45%, #102a6e 75%),
                linear-gradient(160deg, #1a3f9e, #3b6f6a);
    background-blend-mode: normal;
  }
  .back-visual::after {
    content: ""; position: absolute; inset: 0;
    background: linear-gradient(200deg, rgba(90,140,110,.55) 0%, rgba(0,0,0,0) 45%);
  }
  .back-wave { position: absolute; left: 0; bottom: 0; width: 540px; height: 360px; }
  .back-info {
    position: absolute; left: 40px; right: 40px; top: 470px;
    text-align: center; color: var(--ink);
  }
  .brand {
    display: inline-flex; align-items: center; gap: 8px;
    font-family: "Open Sans", Arial, sans-serif; font-weight: 700;
    font-size: 30px; color: var(--brand-blue); letter-spacing: -0.5px;
  }
  .brand-dot { width: 22px; height: 22px; border-radius: 50%; background: var(--brand-green); }
  .brand-sub { display: block; font-size: 10px; font-weight: 400; color: var(--brand-blue); margin: -4px 0 0 30px; text-align: left; }
  .back-info .brand-block { display: inline-block; margin-bottom: 16px; }
  .back-info p { font-size: 14px; line-height: 1.5; margin-bottom: 12px; }
  .back-info .email { display: block; font-weight: 700; font-size: 17px; color: var(--brand-blue); }
  .back-info .site { font-weight: 700; font-size: 17px; color: var(--brand-blue); }
  .back-info .visit { font-size: 16px; }

  /* Front page */
  .front-art { position: absolute; inset: 0; }
  .front-brand { position: absolute; left: 36px; top: 60px; }
  .front-brand .brand { font-size: 32px; }
  .headline {
    position: absolute; left: 30px; right: 0; top: 500px;
    font-family: "Cinzel", Georgia, serif; color: var(--paper); text-transform: uppercase;
  }
  .headline .line-1 { display: block; font-size: 30px; padding: 8px 0 4px 14px; color: var(--deep-blue); }
  .headline .line-2 {
    display: inline-block; background: var(--brand-blue); font-size: 20px;
    padding: 4px 14px; margin-left: 14px;
  }
  .headline .line-3 { display: block; font-size: 42px; font-weight: 700; padding: 4px 0 0 14px; }
  .phone {
    position: absolute; right: 28px; top: 668px;
    display: flex; align-items: center; gap: 8px;
    font-weight: 700; font-size: 20px; color: var(--ink);
  }
  .website {
    position: absolute; left: 0; top: 706px; width: 290px; height: 40px;
    background: var(--brand-blue); color: var(--paper);
    font-family: "Cinzel", Georgia, serif; font-weight: 700; font-size: 17px;
    display: flex; align-items: center; padding-left: 40px; letter-spacing: 1px;
  }
  .footer-green { position: absolute; left: 290px; right: 0; top: 706px; height: 40px; background: var(--brand-green); }
</style>
</head>
<body>
  <main class="spread">
    <section class="page back-page" aria-label="Back page">
      <div class="back-visual" role="img" aria-label="Blue DNA double helix illustration"></div>
      <svg class="back-wave" viewBox="0 0 540 360" preserveAspectRatio="none" aria-hidden="true">
        <defs>
          <linearGradient id="paperFade" x1="0" y1="0" x2="0" y2="1">
            <stop offset="0" stop-color="#f4f5f7"/>
            <stop offset="1" stop-color="#e3e6ea"/>
          </linearGradient>
        </defs>
        <path d="M0 70 C140 20 300 10 540 40 L540 360 L0 360 Z" fill="url(#paperFade)"/>
      </svg>
      <div class="back-info">
        <div class="brand-block">
          <span class="brand"><span class="brand-dot"></span>velicor</span>
          <span class="brand-sub">Personalised health &amp; wellness</span>
        </div>
        <p>For more information about velicor™ or our products, please talk to your local retailer or email us at
          <span class="email">enquiries@velicor.co</span></p>
        <p>Please note test availability may differ from region to region and is subject to availability. Please talk to your local retailer for more information. For a list of approved velicor™ retailers</p>
        <p class="visit">please visit <span class="site">www.velicor.co</span></p>
      </div>
    </section>

    <section class="page front-page" aria-label="Front page">
      <svg class="front-art" viewBox="0 0 540 764" aria-hidden="false">
        <defs>
          <linearGradient id="peopleFill" x1="0" y1="0" x2="1" y2="1">
            <stop offset="0" stop-color="#c9d6e2"/><stop offset="1" stop-color="#6f8aa3"/>
          </linearGradient>
          <linearGradient id="dnaFill" x1="0" y1="0" x2="1" y2="1">
            <stop offset="0" stop-color="#6f9fd6"/><stop offset="1" stop-color="#1f4a86"/>
          </linearGradient>
        </defs>
        <path d="M300 0 C330 110 300 160 250 190 M330 120 C420 170 450 240 430 300" stroke="var(--brand-blue)" stroke-width="18" fill="none"/>
        <path d="M150 440 C170 480 220 490 260 470" stroke="var(--brand-blue)" stroke-width="14" fill="none"/>
        <circle cx="420" cy="30" r="100" fill="var(--photo-lab)" stroke="var(--brand-blue)" stroke-width="10" role="img" aria-label="Lab photograph: gloved hands with pipette"/>
        <circle cx="210" cy="320" r="135" fill="url(#peopleFill)" stroke="var(--brand-blue)" stroke-width="12" role="img" aria-label="Photograph of two scientists at a microscope"/>
        <circle cx="560" cy="350" r="120" fill="url(#dnaFill)" stroke="var(--brand-blue)" stroke-width="12" role="img" aria-label="Close-up DNA strand image"/>
        <path d="M30 500 L540 490 L540 700 L30 700 Z" fill="var(--brand-green)"/>
      </svg>
      <div class="front-brand">
        <span class="brand"><span class="brand-dot"></span>velicor</span>
        <span class="brand-sub">Personalised health &amp; wellness</span>
      </div>
      <h1 class="headline">
        <span class="line-1">We're Helping</span>
        <span class="line-2">To Build the Future of</span>
        <span class="line-3">Good Health</span>
      </h1>
      <div class="phone">
        <svg width="20" height="20" viewBox="0 0 24 24" aria-hidden="true"><path fill="#2b3a55" d="M6.6 10.8a15.1 15.1 0 0 0 6.6 6.6l2.2-2.2c.3-.3.7-.4 1-.2 1.1.4 2.3.6 3.6.6.6 0 1 .4 1 1V20c0 .6-.4 1-1 1A17 17 0 0 1 3 4c0-.6.4-1 1-1h3.5c.6 0 1 .4 1 1 0 1.3.2 2.5.6 3.6.1.3 0 .7-.2 1z"/></svg>
        555-014-2290
      </div>
      <div class="website">WWW.VELICOR.CO</div>
      <div class="footer-green"></div>
    </section>
  </main>
</body>
</html>
```